KTL Stewardship Powerpoint project

Hello, I would like a highly professional powerpoint design that uses the new logo that we had designed for my consulting company. I have created a starting point in powerpoint but the successful designer must take it to a new level. i would like to see a professional image on the front page as well as our website address on a banner at the bottom (www.ktlstewardship.com.au). It is going to be the document we use for presentations that will introduce my company so it must be special!

Industry/Entity Type

It Company

Requirements
Nice to have
• Some sort of design in the front page - attached is company logo for your use.

```html
<!DOCTYPE html>
<html lang="en">
<head>
<meta charset="utf-8">
<title>KTL Stewardship – Presentation Title Slide</title>
<link rel="stylesheet" href="https://fonts.googleapis.com/css2?family=Carlito:ital,wght@0,400;1,400&display=swap">
<style>
  :root {
    --page: #e6e8ec;
    --frame: #ffffff;
    --panel-top: #c4d8f2;
    --panel-bottom: #7aaee8;
    --stage-top: #7f9fca;
    --stage-mid: #6f9ad6;
    --stage-bottom: #8db6ea;
    --stage-edge: #9bb8de;
    --rule-teal: #4fc0a0;
    --rule-green: #2f9e6e;
    --band-navy: #0a5798;
    --strip-blue: #3f8fd0;
    --strip-light: #a6d2f2;
    --mosaic-green: #8cc83c;
    --mosaic-lime: #c6e25a;
    --artwork: #d5d6d8;
    --artwork-tone: #a9aaac;
    --ink: #1b1b1b;
    --ink-navy: #1a1f5e;
    --brand: #2d6fc4;
  }
  * { margin: 0; padding: 0; box-sizing: border-box; }
  html, body { width: 1200px; height: 968px; overflow: hidden; }
  body {
    background: var(--page);
    font-family: "Carlito", "Calibri", sans-serif;
    position: relative;
  }
  .slide-frame {
    position: absolute; left: 23px; top: 23px; width: 1158px; height: 880px;
    background: var(--frame);
    box-shadow: 0 2px 10px rgba(0,0,0,.25);
  }
  .slide-panel {
    position: absolute; left: 63px; top: 50px; width: 1095px; height: 762px;
    background: linear-gradient(180deg, var(--panel-top) 0%, #a9c8ef 40%, var(--panel-bottom) 100%);
  }
  .brand-name {
    position: absolute; right: 50px; top: 64px;
    display: flex; align-items: center; gap: 8px;
    color: var(--brand); font-size: 24px; font-weight: 400;
  }
  .brand-name .brand-square { width: 14px; height: 14px; background: var(--brand); }
  .rule-top {
    position: absolute; left: 108px; top: 127px; width: 978px; height: 2px;
    background: var(--rule-teal);
  }
  .content-stage {
    position: absolute; left: 108px; top: 132px; width: 978px; height: 635px;
    background:
      linear-gradient(180deg, rgba(255,255,255,0) 30%, rgba(255,255,255,.12) 45%, rgba(255,255,255,0) 60%),
      linear-gradient(180deg, var(--stage-top) 0%, var(--stage-mid) 50%, var(--stage-bottom) 100%);
    border: 1px solid var(--stage-edge);
    box-shadow: 0 1px 4px rgba(0,0,0,.2);
  }
  .rule-bottom {
    position: absolute; left: 108px; top: 779px; width: 978px; height: 4px;
    background: var(--rule-green);
  }
  .sample-text {
    position: absolute; left: 146px; top: 290px;
    color: var(--ink); font-size: 34px; line-height: 46px;
  }
  .feature-artwork {
    position: absolute; left: 334px; top: 203px; width: 523px; height: 214px;
    background:
      radial-gradient(circle at 17% 50%, rgba(150,151,153,.55) 0 60px, transparent 78px),
      radial-gradient(circle at 50% 50%, rgba(150,151,153,.55) 0 60px, transparent 78px),
      radial-gradient(circle at 83% 50%, rgba(150,151,153,.55) 0 60px, transparent 78px),
      repeating-linear-gradient(0deg, rgba(255,255,255,.12) 0 1px, transparent 1px 3px),
      repeating-linear-gradient(90deg, rgba(0,0,0,.04) 0 1px, transparent 1px 3px),
      linear-gradient(180deg, #dcdddf, var(--artwork));
  }
  .feature-reflection {
    position: absolute; left: 334px; top: 424px; width: 523px; height: 150px;
    background:
      radial-gradient(ellipse 70px 60px at 17% 0%, rgba(150,151,153,.45), transparent),
      radial-gradient(ellipse 70px 60px at 50% 0%, rgba(150,151,153,.45), transparent),
      radial-gradient(ellipse 70px 60px at 83% 0%, rgba(150,151,153,.45), transparent),
      linear-gradient(180deg, rgba(213,214,216,.7), rgba(213,214,216,0));
  }
  .footer-band {
    position: absolute; left: 23px; top: 812px; width: 1158px; height: 30px;
    background: var(--band-navy);
  }
  .footer-strip {
    position: absolute; left: 23px; top: 842px; width: 1158px; height: 57px;
  }
  .footer-graphic {
    position: absolute; left: 0; top: 0; width: 684px; height: 57px;
    background: linear-gradient(90deg, var(--strip-light) 0%, var(--strip-blue) 18%, #5fa6dc 55%, var(--strip-light) 100%);
  }
  .footer-mosaic {
    position: absolute; left: 687px; top: 0; width: 471px; height: 57px;
    background: linear-gradient(90deg, var(--mosaic-lime), var(--mosaic-green) 45%, var(--mosaic-lime) 100%);
  }
  .tagline {
    position: absolute; left: 337px; top: 15px;
    font-style: italic; font-size: 23px; color: var(--ink);
    border-bottom: 1px solid var(--ink); padding: 0 6px 1px;
  }
  .web-address {
    position: absolute; left: 742px; top: 12px;
    font-size: 27px; color: var(--ink-navy);
  }
  .footer-reflection {
    position: absolute; left: 23px; top: 903px; width: 1158px; height: 38px;
    background: linear-gradient(180deg, rgba(90,150,210,.35), rgba(90,150,210,0));
  }
</style>
</head>
<body>
  <div class="slide-frame"></div>
  <div class="slide-panel"></div>

  <div class="brand-name"><span class="brand-square"></span>KTL Stewardship</div>

  <div class="rule-top"></div>
  <div class="content-stage"></div>
  <div class="rule-bottom"></div>

  <div class="feature-artwork" role="img" aria-label="Grey linen panel of three stylised tribal motifs: a bird-like figure, a round sunburst and a heron"></div>
  <div class="feature-reflection" role="img" aria-label="Faded mirror reflection of the tribal motif panel"></div>

  <p class="sample-text">Abcdefg<br>1234567890</p>

  <div class="footer-band"></div>
  <div class="footer-strip">
    <div class="footer-graphic" role="img" aria-label="Blue abstract swirl banner graphic"></div>
    <div class="footer-mosaic" role="img" aria-label="Green and lime pixel mosaic pattern"></div>
    <span class="tagline">A better result</span>
    <span class="web-address">www.ktlstewardship.com.au</span>
  </div>
  <div class="footer-reflection"></div>
</body>
</html>
```